Executive Business Card for Healthcare Company [Need Today]

I need a business card design for a healthcare company. The only branding the company has thus far is a logo. The cards will be utilized by company executives. The design I envision will be vibrant and appealing but with a corporate feel. They shouldn't be too casual or playful. I would like to complete this project TODAY if possible.

Target Market(s)

Healthcare vendors, other executives in healthcare and pharmaceuticals

Industry/Entity Type

Pharmaceutical

Contact Information for Business Card

See attachment

Font styles to use
Serif
Sans Serif

Colors

Designer to choose colors to be used in the design.

```html
<!DOCTYPE html>
<html lang="en">
<head>
<meta charset="utf-8">
<title>Meridell Therapeutics – Business Card</title>
<link rel="stylesheet" href="https://fonts.googleapis.com/css2?family=Open+Sans:wght@300;400;700&display=swap">
<style>
  :root {
    --teal: #3fb4ba;
    --teal-dark: #35a8ae;
    --green: #5cb88f;
    --ink: #4a4a4a;
    --rule: #7a7a7a;
    --card-white: #f4f4f4;
    --stage: #e6e8ea;
  }
  * { margin: 0; padding: 0; box-sizing: border-box; }
  html, body {
    width: 1200px; height: 900px; overflow: hidden;
    background: var(--stage);
    font-family: "Open Sans", Arial, sans-serif;
  }
  .sheet {
    position: relative; width: 1200px; height: 900px;
  }
  .card {
    position: absolute; left: 250px; width: 700px; height: 400px;
    box-shadow: 0 6px 18px rgba(0,0,0,0.12);
  }
  .card--front {
    top: 30px;
    background: linear-gradient(135deg, var(--teal-dark), var(--teal));
  }
  .card--back {
    top: 470px;
    background: var(--card-white);
  }
  .brand {
    position: absolute; display: flex; align-items: center;
  }
  .brand__mark {
    border-radius: 50%; border: 3px solid currentColor; flex: none;
  }
  .brand__divider {
    width: 1px; align-self: stretch; margin: 14px 14px; background: currentColor; opacity: .7;
  }
  .brand__name {
    font-weight: 300; line-height: 1.05; letter-spacing: .5px;
  }
  .card--front .brand {
    color: #fff; left: 50%; top: 50%; transform: translate(-50%, -50%);
  }
  .card--front .brand__mark { width: 96px; height: 96px; }
  .card--front .brand__name { font-size: 34px; }
  .card--back .brand {
    left: 44px; top: 142px; color: var(--teal);
  }
  .card--back .brand__mark { width: 96px; height: 96px; border-color: var(--green); }
  .card--back .brand__name { font-size: 30px; }
  .card--back .brand__divider { background: var(--rule); }
  .card__rule {
    position: absolute; left: 392px; top: 92px; width: 2px; height: 226px; background: var(--rule);
  }
  .contact {
    position: absolute; left: 424px; top: 96px; color: var(--ink);
  }
  .contact__name {
    font-size: 22px; font-weight: 700; color: var(--green); line-height: 1.2;
  }
  .contact__title {
    font-size: 17px; margin-bottom: 16px;
  }
  .contact__address {
    font-size: 17px; line-height: 1.4; margin-bottom: 14px; font-style: normal;
  }
  .contact__line {
    display: flex; align-items: center; gap: 10px; font-size: 18px; line-height: 1.45;
  }
  .contact__line svg { width: 16px; height: 16px; flex: none; color: var(--teal); }
</style>
</head>
<body>
<main class="sheet">
  <section class="card card--front" aria-label="Card front">
    <div class="brand">
      <span class="brand__mark"></span>
      <span class="brand__divider"></span>
      <span class="brand__name">meridell<br>therapeutics</span>
    </div>
  </section>

  <section class="card card--back" aria-label="Card back">
    <div class="brand">
      <span class="brand__mark"></span>
      <span class="brand__divider"></span>
      <span class="brand__name">meridell<br>therapeutics</span>
    </div>
    <div class="card__rule"></div>
    <div class="contact">
      <p class="contact__name">Daniel Foster</p>
      <p class="contact__title">Senior Director of Marketing</p>
      <address class="contact__address">Meridell Therapeutics, LLC<br>118 N Lumpkin Avenue<br>Riverton, GA 30999</address>
      <p class="contact__line">
        <svg viewBox="0 0 16 16" aria-hidden="true"><path fill="currentColor" d="M3.6 1.5l2.2 2.4-1.3 1.6c.9 2 2.4 3.5 4.4 4.4l1.6-1.3 2.4 2.2-1.4 2.2C6.6 12.8 3.2 9.4 1.4 4.5z"/></svg>
        555-210-4837
      </p>
      <p class="contact__line">
        <svg viewBox="0 0 16 16" aria-hidden="true"><rect x="4" y="1" width="8" height="14" rx="1.5" fill="none" stroke="currentColor" stroke-width="1.5"/><line x1="7" y1="12.5" x2="9" y2="12.5" stroke="currentColor" stroke-width="1.5"/></svg>
        555-318-6042
      </p>
      <p class="contact__line">
        <svg viewBox="0 0 16 16" aria-hidden="true"><rect x="1" y="3.5" width="14" height="10" rx="1" fill="currentColor"/><path d="M1.5 4l6.5 5 6.5-5" fill="none" stroke="#fff" stroke-width="1.3"/></svg>
        dfoster@meridellrx.com
      </p>
    </div>
  </section>
</main>
</body>
</html>
```